Meadowrun Honey labels

I have honey farm . I would like to sale it at grocery stores. I need really unique and very attractive designed labels, I would like to see writings 100% Natural honey and GMO free ,. Company name "MeadowrunHoney" . I want to put 2 labels and one ribbon tag in middle and round label on top of lid(only one diamond shape in the middle).I would like to see bee flying over red flower and at the left side flower field and right side bee putting honey into honey hives. I have attached example pictures of Honey Jars labels, tags and type. I have two different type of Honey jars i have also attached picture of those jars. For jar with red lid. If middle label little bit bigger than measurement thats ok because writing has to fit.

Target Market(s)

Grocery stores

Industry/Entity Type

Farm

Requirements
Must have
• 100% Natural Honey, GMO Free, Company name Meadowrun Honey, attractive and unique design. bee flying over flower, right side label flower field left side bee putting honey into bee hives.

```html
<!DOCTYPE html>
<html lang="en">
<head>
<meta charset="utf-8">
<title>Meadowrun Honey labels</title>
<link rel="stylesheet" href="https://fonts.googleapis.com/css2?family=Archivo+Black&family=Arimo:wght@700&display=swap">
<style>
  :root {
    --backdrop: #3a3a3e;
    --honey-orange: #f7a21b;
    --honey-deep: #f08c00;
    --honey-yellow: #ffe033;
    --comb-pale: #fde58a;
    --comb-warm: #fbd34d;
    --cream: #ffffff;
    --label-edge: #fff3c4;
    --claim-red: #8a1a12;
    --claim-orange: #f29a1a;
  }
  html, body {
    margin: 0;
    padding: 0;
    width: 1200px;
    height: 1000px;
    overflow: hidden;
    background: var(--backdrop);
  }
  .label-sheet {
    position: relative;
    width: 1200px;
    height: 1000px;
  }
  .label-sheet svg {
    position: absolute;
    inset: 0;
    width: 1200px;
    height: 1000px;
  }
  .brand-name {
    font-family: "Archivo Black", "Arial Black", sans-serif;
    fill: var(--honey-deep);
    text-anchor: middle;
  }
  .claim {
    font-family: "Arimo", Arial, sans-serif;
    font-weight: 700;
  }
  .claim-natural { fill: var(--claim-red); }
  .claim-gmo { fill: var(--claim-orange); }
</style>
</head>
<body>
<main class="label-sheet">
  <svg viewBox="0 0 1200 1000" xmlns="http://www.w3.org/2000/svg">
    <defs>
      <radialGradient id="lid-face" cx="50%" cy="50%" r="50%">
        <stop offset="0%" stop-color="var(--cream)"/>
        <stop offset="70%" stop-color="#fffbe8"/>
        <stop offset="100%" stop-color="var(--label-edge)"/>
      </radialGradient>
      <linearGradient id="ribbon-fill" x1="0" x2="1" y1="0" y2="0">
        <stop offset="0%" stop-color="var(--honey-orange)"/>
        <stop offset="38%" stop-color="var(--honey-yellow)"/>
        <stop offset="62%" stop-color="var(--honey-yellow)"/>
        <stop offset="100%" stop-color="var(--honey-orange)"/>
      </linearGradient>
      <linearGradient id="comb-band-fill" x1="0" x2="1" y1="0" y2="1">
        <stop offset="0%" stop-color="var(--comb-warm)"/>
        <stop offset="50%" stop-color="var(--comb-pale)"/>
        <stop offset="100%" stop-color="var(--comb-warm)"/>
      </linearGradient>
      <radialGradient id="comb-glow" cx="55%" cy="45%" r="50%">
        <stop offset="0%" stop-color="var(--comb-warm)" stop-opacity="0.9"/>
        <stop offset="60%" stop-color="var(--comb-pale)" stop-opacity="0.6"/>
        <stop offset="100%" stop-color="var(--comb-pale)" stop-opacity="0"/>
      </radialGradient>
    </defs>

    <g class="lid-label">
      <circle cx="600" cy="311" r="170" fill="var(--honey-orange)"/>
      <circle cx="600" cy="311" r="160" fill="var(--cream)"/>
      <circle cx="600" cy="311" r="154" fill="url(#lid-face)"/>
      <ellipse class="comb-decoration" cx="610" cy="300" rx="135" ry="110" fill="url(#comb-glow)"
               role="img" aria-label="Honeycomb cells scattered behind the brand name"/>
      <text class="brand-name" x="600" y="294" font-size="34">MEADOWRUN</text>
      <text class="brand-name" x="600" y="345" font-size="50">HONEY</text>
      <text class="claim claim-natural" x="590" y="364" font-size="12">100% Natural Honey</text>
      <text class="claim claim-gmo" x="624" y="379" font-size="12">GMO Free</text>
    </g>

    <g class="ribbon-tag">
      <rect x="202" y="630" width="796" height="82" fill="url(#ribbon-fill)"/>
      <rect x="202" y="630" width="796" height="6" fill="var(--honey-deep)"/>
      <rect x="202" y="706" width="796" height="6" fill="var(--honey-deep)"/>
      <rect class="comb-band" x="222" y="636" width="196" height="70" fill="url(#comb-band-fill)"
            role="img" aria-label="Honeycomb pattern on the left of the ribbon"/>
      <rect class="comb-band" x="782" y="636" width="196" height="70" fill="url(#comb-band-fill)"
            role="img" aria-label="Honeycomb pattern on the right of the ribbon"/>

      <polygon points="599,543 728,590 728,750 599,798 470,750 470,590" fill="var(--honey-orange)"/>
      <polygon points="599,556 718,598 718,742 599,785 480,742 480,598" fill="var(--cream)"/>
      <polygon points="599,563 711,603 711,737 599,778 487,737 487,603"
               fill="none" stroke="var(--honey-orange)" stroke-width="1"/>
      <ellipse class="comb-decoration" cx="605" cy="665" rx="100" ry="90" fill="url(#comb-glow)"
               role="img" aria-label="Honeycomb cells scattered behind the brand name"/>
      <text class="brand-name" x="599" y="665" font-size="26">MEADOWRUN</text>
      <text class="brand-name" x="599" y="704" font-size="38">HONEY</text>
      <text class="claim claim-natural" x="591" y="720" font-size="10">100% Natural Honey</text>
      <text class="claim claim-gmo" x="618" y="733" font-size="10">GMO Free</text>
    </g>
  </svg>
</main>
</body>
</html>
```